Lumora Digital - Layout Design

We need a web design for a new company based in Australia, called "Lumora Digital". We develop innovative custom web applications for Out Of Home, and Media companies.
Our initial website is a one page type of site. I've created a simple wireframe to show you what we need: https://sketchplot.example/k3Tq9W
Here is a layout reference: http://folvex.example/
( note - the designs needs to follow our branding guidelines (attached).
The top feature could be just solid color or an abstract subtle pattern or illustration that conveys the specialization of our business in the area of out of home, map, data.
In the attachment you will also find some images added for the work section.
Updates
Target Market(s)
Media and Advertising
Industry/Entity Type
Digital
Number of Pages Required
1 page
Look and feel
Each slider illustrates characteristics of the customer's brand and the style your logo design should communicate.

```html
<!DOCTYPE html>
<html lang="en">
<head>
<meta charset="utf-8">
<title>Lumora Digital</title>
<link href="https://fonts.googleapis.com/css2?family=Open+Sans:wght@300;400;600;700&display=swap" rel="stylesheet">
<style>
:root{
  --white:#ffffff;
  --ink:#2b2b2b;
  --accent:#f0533f;
  --about:#1e9be8;
  --team:#d9a62a;
  --board:#c455c9;
  --services:#f0533f;
  --experience:#8d7cf0;
  --contact:#000000;
}
*{margin:0;padding:0;box-sizing:border-box}
html,body{width:1200px;height:3548px;overflow:hidden}
body{font-family:"Open Sans",Arial,sans-serif;color:var(--white);background:var(--white)}
.section{position:relative;width:1200px;text-align:center}
.section-title{font-weight:300;font-size:40px;line-height:48px;display:inline-flex;align-items:center;gap:10px}
.title-mark{width:18px;height:14px;border:2px solid currentColor;border-radius:3px;display:inline-block}
.copy{font-size:12.5px;line-height:20px;font-weight:400}
.btn{display:inline-block;border:1px solid var(--white);color:var(--white);font-size:11px;padding:8px 26px;text-decoration:none}

/* hero */
.hero{height:720px;background:linear-gradient(120deg,#d9d3cb 0%,#b9a99a 30%,#8e7d72 55%,#c9bfb6 80%,#e8e2db 100%)}
.site-header{position:absolute;top:0;left:0;width:1200px;height:80px;display:flex;justify-content:space-between;align-items:stretch}
.brand{display:flex;align-items:center;padding:0 28px;background:rgba(255,255,255,.85);color:var(--ink);font-size:30px;font-weight:400}
.main-nav{display:flex;margin-right:60px}
.main-nav a{color:var(--white);text-decoration:none;font-size:11px;font-weight:600;padding:0 22px;display:flex;align-items:center}
.main-nav a.active{background:var(--accent)}
.hero-caption{position:absolute;left:560px;top:360px;width:600px;text-align:left}
.hero-caption h1{font-weight:300;font-size:46px;line-height:50px;text-transform:uppercase;letter-spacing:1px;text-shadow:0 1px 3px rgba(0,0,0,.3)}
.hero-caption p{font-size:13px;line-height:19px;margin-top:10px;width:560px}
.slider-dots{position:absolute;left:1020px;top:615px;display:flex;gap:12px}
.slider-dots span{width:11px;height:11px;border-radius:50%;border:2px solid var(--white)}
.slider-dots span.on{background:var(--white)}

.about{height:328px;background:var(--about);padding-top:40px}
.about .copy{width:1040px;margin:18px auto 26px}

.team{height:440px;background:var(--team);padding-top:40px}
.board{height:532px;background:var(--board);padding-top:40px}
.people{display:flex;justify-content:center}
.person{width:350px;margin:0 25px;display:flex;flex-direction:column;align-items:center}
.avatar{width:112px;height:112px;border-radius:50%;border:3px solid rgba(255,255,255,.8);background:radial-gradient(circle at 50% 40%,#5b6472,#1f2430)}
.person-name{font-size:12px;font-weight:700;margin:14px 0 8px}
.person .copy{font-size:11.5px;line-height:17px;margin-bottom:22px}
.team .people{margin-top:40px}
.board-intro{width:1000px;margin:14px auto 0}
.board .people{margin-top:36px}
.board .person{width:440px;margin:0 70px}

.services{height:340px;background:var(--services);padding-top:46px}
.services .copy{width:1040px;margin:18px auto 34px}

.experience{height:872px;background:var(--experience);padding-top:30px}
.cards{display:grid;grid-template-columns:repeat(3,352px);gap:26px 24px;justify-content:center;margin-top:22px}
.card{display:flex;flex-direction:column;align-items:center}
.card-media{width:352px;height:196px}
.card-title{font-size:20px;font-weight:400;margin:14px 0 6px}
.card .copy{font-size:11px;line-height:16px;margin-bottom:16px;padding:0 10px}
.m1{background:linear-gradient(135deg,#23508f,#6fb0e0)}
.m2{background:linear-gradient(135deg,#d8b8a0,#9c7a66)}
.m3{background:linear-gradient(135deg,#e9ecef,#9aa6b2)}
.m4{background:linear-gradient(135deg,#c4c1be,#7a7470)}
.m5{background:linear-gradient(135deg,#1a4d8f,#5fa8e6)}
.m6{background:linear-gradient(160deg,#8fb8e0,#d9c27a 70%,#e1a03a)}

.contact{height:316px;background:var(--contact);padding-top:40px}
.contact .copy{font-size:11px;line-height:18px;margin-top:12px}
</style>
</head>
<body>

<section class="section hero" role="img" aria-label="Photo of young people smiling around a laptop outdoors">
  <header class="site-header">
    <div class="brand">Lumora Digital</div>
    <nav class="main-nav">
      <a class="active" href="#about">ABOUT US</a>
      <a href="#team">TEAM</a>
      <a href="#services">SERVICES</a>
      <a href="#experience">EXPERIENCE</a>
      <a href="#contact">CONTACT</a>
    </nav>
  </header>
  <div class="hero-caption">
    <h1>Consectetur adipiscing<br>lorem ipsum dolor</h1>
    <p>We build custom web applications for out of home and media companies, turning places, maps and audience data into clear, useful tools.</p>
  </div>
  <div class="slider-dots"><span class="on"></span><span></span><span></span><span></span></div>
</section>

<section class="section about" id="about">
  <h2 class="section-title">About us <span class="title-mark"></span></h2>
  <p class="copy">Lumora Digital is an Australian studio creating innovative custom web applications for out of home and media companies. We combine location data, mapping and audience insight to help our clients plan, sell and measure their campaigns with confidence. Our small team of designers and developers works closely with every partner, from first sketch to launch, and keeps improving each product long after it goes live. We value clarity, speed and tools that people actually enjoy using every day across their business.</p>
  <a class="btn" href="#about">Read More</a>
</section>

<section class="section team" id="team">
  <h2 class="section-title">Key Team <span class="title-mark"></span></h2>
  <div class="people">
    <div class="person">
      <div class="avatar" role="img" aria-label="Portrait photo of team member"></div>
      <div class="person-name">NORA VASKEL - CEO</div>
      <p class="copy">Nora leads strategy and client relationships, bringing years of experience in outdoor media and product design to every project our team delivers for partners.</p>
      <a class="btn" href="#team">READ MORE</a>
    </div>
    <div class="person">
      <div class="avatar" role="img" aria-label="Portrait photo of team member"></div>
      <div class="person-name">NORA VASKEL - CEO</div>
      <p class="copy">Nora leads strategy and client relationships, bringing years of experience in outdoor media and product design to every project our team delivers for partners.</p>
      <a class="btn" href="#team">READ MORE</a>
    </div>
    <div class="person">
      <div class="avatar" role="img" aria-label="Portrait photo of team member"></div>
      <div class="person-name">NORA VASKEL - CEO</div>
      <p class="copy">Nora leads strategy and client relationships, bringing years of experience in outdoor media and product design to every project our team delivers for partners.</p>
      <a class="btn" href="#team">READ MORE</a>
    </div>
  </div>
</section>

<section class="section board">
  <h2 class="section-title">Board of Advisors <span class="title-mark"></span></h2>
  <p class="copy board-intro">Our advisors bring deep knowledge of media, advertising and technology. They guide our growth, challenge our thinking and help us build products that serve the whole industry well.</p>
  <div class="people">
    <div class="person">
      <div class="avatar" role="img" aria-label="Portrait photo of advisor"></div>
      <div class="person-name">NORA VASKEL - CEO</div>
      <p class="copy">Nora has advised media groups across Australia and Asia on digital change. She helps our team shape long term product plans and keeps our work focused on real client needs.</p>
      <a class="btn" href="#team">READ MORE</a>
    </div>
    <div class="person">
      <div class="avatar" role="img" aria-label="Portrait photo of advisor"></div>
      <div class="person-name">NORA VASKEL - CEO</div>
      <p class="copy">Nora has advised media groups across Australia and Asia on digital change. She helps our team shape long term product plans and keeps our work focused on real client needs.</p>
      <a class="btn" href="#team">READ MORE</a>
    </div>
  </div>
</section>

<section class="section services" id="services">
  <h2 class="section-title">Our Services <span class="title-mark"></span></h2>
  <p class="copy">We specialise in all sorts of integration matters such as campaign planning tools, inventory and availability systems, interactive site maps, audience data dashboards, proof of posting workflows, sales proposal builders, client portals and reporting suites. Every application is designed around your team, your data and your screens, and is built to grow with your business over time.</p>
  <a class="btn" href="#services">Read More</a>
</section>

<section class="section experience" id="experience">
  <h2 class="section-title">Experience <span class="title-mark"></span></h2>
  <div class="cards">
    <div class="card"><div class="card-media m1" role="img" aria-label="Photo of hands with a glowing cloud network graphic"></div><h3 class="card-title">Arcline Outdoor</h3><p class="copy">A custom planning platform that maps every outdoor site, shows live availability and builds client proposals in minutes.</p><a class="btn" href="#experience">READ MORE</a></div>
    <div class="card"><div class="card-media m2" role="img" aria-label="Photo of smiling couple looking at a laptop"></div><h3 class="card-title">Arcline Outdoor</h3><p class="copy">A custom planning platform that maps every outdoor site, shows live availability and builds client proposals in minutes.</p><a class="btn" href="#experience">READ MORE</a></div>
    <div class="card"><div class="card-media m3" role="img" aria-label="Photo of a hand touching a tablet screen"></div><h3 class="card-title">Arcline Outdoor</h3><p class="copy">A custom planning platform that maps every outdoor site, shows live availability and builds client proposals in minutes.</p><a class="btn" href="#experience">READ MORE</a></div>
    <div class="card"><div class="card-media m4" role="img" aria-label="Photo of a hand using a smartphone"></div><h3 class="card-title">Arcline Outdoor</h3><p class="copy">A custom planning platform that maps every outdoor site, shows live availability and builds client proposals in minutes.</p><a class="btn" href="#experience">READ MORE</a></div>
    <div class="card"><div class="card-media m5" role="img" aria-label="Photo of a laptop with a cloud network graphic"></div><h3 class="card-title">Arcline Outdoor</h3><p class="copy">A custom planning platform that maps every outdoor site, shows live availability and builds client proposals in minutes.</p><a class="btn" href="#experience">READ MORE</a></div>
    <div class="card"><div class="card-media m6" role="img" aria-label="Photo of a construction worker in front of a tower"></div><h3 class="card-title">Arcline Outdoor</h3><p class="copy">A custom planning platform that maps every outdoor site, shows live availability and builds client proposals in minutes.</p><a class="btn" href="#experience">READ MORE</a></div>
  </div>
</section>

<section class="section contact" id="contact">
  <h2 class="section-title">Contact <span class="title-mark"></span></h2>
  <p class="copy">Curious about who we are or how we can help your organisation? Then please get in touch<br>hello@lumoradigital.example<br>or above us<br>Lumora Digital | Pty Ltd | Suite 4, Level 6 | Harbourline Tower | Wren Lane | Sydney NSW 2000 | Australia</p>
</section>

</body>
</html>
```